Tarrow Consulting WA Business Card

Create an interesting, eye catching and colourful two sided business card. We are a business consulting operation assisting SME's improve all areas of their business. We provide consulting services to assist SME's to create a culture of continuous improvement, making a positive difference in the business. Our tag line is Small changes, big rewards. We want to create a well recognised, innovative brand that can be continued throughout our website, social media and email correspondence.

Target Market(s)

Small to Medium Enterprise Business Owners

Industry/Entity Type

Business Consultant

Contact Information for Business Card

Name of Business: Tarrow Consulting - Steady Steps Lasting Gains
Dean Fordyce Ph 0407358114 Moira Fordyce Ph 0407935281
Email tarrowconsultingwa@mailbox-example.com
Web address TBA
FaceBook page TBA

BACKSIDE OF CARD

Providing assistance with:

• Organisation & Efficiency
• Revenue generation & Marketing
• Financial Management
• Production quality & delivery
• Systems & Process documentation
• Exit Strategy

Font styles to use
Other font styles liked:
• Calibri

Colors

Designer to choose colors to be used in the design.

Requirements
Must have
• Calibri font

```html
<!DOCTYPE html>
<html lang="en">
<head>
<meta charset="utf-8">
<title>Tarrow Consulting – Business Card</title>
<link href="https://fonts.googleapis.com/css2?family=Open+Sans:wght@400;600;700&display=swap" rel="stylesheet">
<style>
  :root {
    --page-bg: #2a2a2a;
    --card-red: #d64a3c;
    --card-red-light: #de5d50;
    --card-white: #ffffff;
    --brand-blue: #3b76bf;
    --brand-red: #d9443a;
    --text-grey: #4a4a4a;
    --tone-blue: #4f8fcf;
    --tone-yellow: #f2c53d;
    --tone-green: #8cc43f;
    --tone-orange: #e9a23b;
  }
  * { box-sizing: border-box; margin: 0; padding: 0; }
  html, body { width: 1200px; height: 930px; overflow: hidden; }
  body {
    background: var(--page-bg);
    font-family: 'Open Sans', Calibri, sans-serif;
    display: flex;
    flex-direction: column;
    align-items: center;
    justify-content: center;
    gap: 40px;
  }
  .card {
    position: relative;
    width: 720px;
    height: 411px;
    border-radius: 18px;
    overflow: hidden;
  }

  /* Back side */
  .card--back {
    background: linear-gradient(100deg, var(--card-red) 0%, var(--card-red-light) 35%, var(--card-red) 60%);
    color: #fff;
  }
  .back-brand {
    position: absolute;
    left: 178px;
    top: 120px;
    display: flex;
    align-items: center;
    gap: 22px;
  }
  .back-brand__mark {
    width: 64px;
    height: 64px;
    border-radius: 50%;
    background: #fff;
  }
  .back-brand__name {
    font-size: 36px;
    font-weight: 700;
    line-height: 1;
  }
  .back-brand__tagline {
    font-size: 20px;
    font-weight: 400;
    margin-top: 6px;
    padding-left: 22px;
  }
  .services {
    position: absolute;
    left: 0;
    right: 0;
    top: 250px;
    list-style: none;
    text-align: center;
    font-size: 16px;
    line-height: 1.45;
  }

  /* Front side */
  .card--front { background: var(--card-white); }
  .front-art {
    position: absolute;
    right: 0;
    top: 0;
    width: 320px;
    height: 300px;
  }
  .front-brand {
    position: absolute;
    left: 56px;
    top: 112px;
  }
  .front-brand__name {
    font-size: 36px;
    font-weight: 700;
    color: var(--brand-blue);
    line-height: 1;
  }
  .front-brand__tagline {
    font-size: 21px;
    color: var(--brand-red);
    padding-left: 22px;
    margin-top: 4px;
  }
  .partners {
    position: absolute;
    left: 148px;
    top: 212px;
    font-size: 25px;
    font-weight: 600;
    color: var(--brand-blue);
    line-height: 1.25;
    text-transform: uppercase;
    list-style: none;
  }
  .partners li:nth-child(2) { padding-left: 22px; }
  .contacts {
    position: absolute;
    left: 196px;
    top: 310px;
    list-style: none;
    font-size: 15px;
    color: var(--text-grey);
    line-height: 1.45;
  }
  .contacts li { display: flex; align-items: center; gap: 8px; }
  .contacts svg { width: 11px; height: 11px; flex: none; }
  .contacts .web-domain { color: var(--brand-blue); font-weight: 600; }
</style>
</head>
<body>

  <section class="card card--back" aria-label="Card back">
    <div class="back-brand">
      <span class="back-brand__mark" aria-hidden="true"></span>
      <div>
        <div class="back-brand__name">Tarrow Consulting</div>
        <div class="back-brand__tagline">Steady Steps Lasting Gains</div>
      </div>
    </div>
    <ul class="services">
      <li>&gt; Organisation &amp; Efficiency &gt; Revenue generation &amp; Marketing</li>
      <li>&gt; Financial Management &gt; Production quality &amp; delivery</li>
      <li>&gt; Systems &amp; Process documentation &gt; Exit Strategy</li>
    </ul>
  </section>

  <section class="card card--front" aria-label="Card front">
    <svg class="front-art" viewBox="0 0 320 300" role="img" aria-label="Colourful decorative brand artwork in blue, yellow, red and green">
      <defs>
        <linearGradient id="artTones" x1="0" y1="0" x2="1" y2="1">
          <stop offset="0" stop-color="var(--tone-blue)"/>
          <stop offset="0.45" stop-color="var(--tone-yellow)"/>
          <stop offset="0.7" stop-color="var(--tone-orange)"/>
          <stop offset="1" stop-color="var(--tone-green)"/>
        </linearGradient>
      </defs>
      <path d="M60 0 H320 V300 C250 300 190 270 140 230 C90 190 40 140 30 80 C25 45 40 15 60 0 Z" fill="url(#artTones)"/>
    </svg>

    <div class="front-brand">
      <div class="front-brand__name">Tarrow Consulting</div>
      <div class="front-brand__tagline">Steady Steps Lasting Gains</div>
    </div>

    <ul class="partners">
      <li>Dean Fordyce</li>
      <li>Moira Fordyce</li>
    </ul>

    <ul class="contacts">
      <li>
        <svg viewBox="0 0 12 12" aria-hidden="true"><path d="M3 1 L5 3.5 L3.8 4.8 C4.5 6.5 5.5 7.5 7.2 8.2 L8.5 7 L11 9 L9.5 11 C5 10.5 1.5 7 1 2.5 Z" fill="var(--brand-blue)"/></svg>
        0407358114
      </li>
      <li>
        <svg viewBox="0 0 12 12" aria-hidden="true"><path d="M3 1 L5 3.5 L3.8 4.8 C4.5 6.5 5.5 7.5 7.2 8.2 L8.5 7 L11 9 L9.5 11 C5 10.5 1.5 7 1 2.5 Z" fill="var(--brand-blue)"/></svg>
        0407935281
      </li>
      <li>
        <svg viewBox="0 0 12 12" aria-hidden="true"><rect x="1" y="2.5" width="10" height="7" fill="none" stroke="var(--brand-blue)" stroke-width="1.4"/><path d="M1 2.5 L6 6.5 L11 2.5" fill="none" stroke="var(--brand-blue)" stroke-width="1.4"/></svg>
        tarrowconsultingwa@mailbox-example.com
      </li>
      <li>
        <svg viewBox="0 0 12 12" aria-hidden="true"><circle cx="6" cy="6" r="5" fill="none" stroke="var(--brand-blue)" stroke-width="1.3"/><ellipse cx="6" cy="6" rx="2.2" ry="5" fill="none" stroke="var(--brand-blue)" stroke-width="1"/><path d="M1 6 H11" stroke="var(--brand-blue)" stroke-width="1"/></svg>
        <span>www.<span class="web-domain">tarrowconsultingwa</span>.com</span>
      </li>
    </ul>
  </section>

</body>
</html>
```